Staffing/Recruitment company

We need to upgrade our website. At the moment we have a template that was built last year and looks not good at all.
We would like to update it with a new design based on what is popular this year. Including some visual effects etc.
This website is to give all information to our potential clients about what we do, clients with worked in the past, how to contact us and about us.
The website consists of 4 pages.
We would like to see a design that uses the color blue.
The current website is https://brightkelvo.us/
Logo of the company is uploaded

Some designs were not complete...

```html
<!DOCTYPE html>
<html lang="en">
<head>
<meta charset="utf-8">
<title>Healthcare Division – Bright Kelvo</title>
<link href="https://fonts.googleapis.com/css2?family=Poppins:wght@400;500;600;700&family=Heebo:wght@300;400;500&display=swap" rel="stylesheet">
<style>
:root{
  --blue:#1f3f9e;
  --blue-dark:#1a3690;
  --orange:#f0582a;
  --ink:#1c1c1c;
  --muted:#6b6b6b;
  --line:#e6e6e6;
  --panel:#f3f3f3;
  --header-bg:#f5f5f5;
  --footer:#222222;
  --footer-bottom:#1c1c1c;
  --footer-text:#9a9a9a;
}
*{margin:0;padding:0;box-sizing:border-box}
html,body{width:805px;height:1200px;overflow:hidden;background:#fff}
body{position:relative;font-family:'Heebo',sans-serif;color:var(--ink)}
.abs{position:absolute}
.topbar{left:0;top:0;width:805px;height:33px;background:var(--blue);color:#fff;font-size:9px}
.topbar .dream{left:54px;top:10px}
.apply{left:159px;top:9px;background:var(--orange);border-radius:8px;padding:2px 7px;font-family:'Poppins',sans-serif;font-weight:600;font-size:7px;letter-spacing:.4px}
.toplinks{right:54px;top:10px;display:flex;gap:0}
.toplinks span{padding:0 7px;border-left:1px solid rgba(255,255,255,.3)}
.toplinks span:first-child{border-left:0}
.header{left:0;top:33px;width:805px;height:98px;background:var(--header-bg)}
.brand{left:54px;top:53px;display:flex;align-items:center;gap:5px;font-family:'Poppins',sans-serif;font-weight:600;font-size:11px;color:var(--blue)}
.brand i{width:7px;height:7px;background:var(--orange);display:block}
.info{font-size:9px;line-height:1.5}
.info em{color:var(--muted);font-weight:300}
.info b{font-weight:500}
.join{left:656px;top:57px;width:98px;height:29px;border:1px solid #e2e2e2;border-radius:15px;background:#fff;font-family:'Poppins',sans-serif;font-weight:600;font-size:8px;letter-spacing:.6px;text-align:center;line-height:27px}
.nav{left:54px;top:111px;width:700px;height:41px;background:#fff;display:flex;align-items:center;padding-left:14px;font-family:'Poppins',sans-serif;font-weight:600;font-size:8px;z-index:2}
.nav span{padding:0 12px;border-right:1px solid var(--line);line-height:10px}
.nav span:first-child{padding-left:0}
.social{right:14px;top:15px;font-family:'Heebo',sans-serif;font-weight:400;font-size:8.5px;color:var(--muted);display:flex;gap:6px;align-items:center}
.social i{width:9px;height:9px;background:#8a8a8a;border-radius:2px;display:block}
.hero{left:0;top:131px;width:805px;height:195px;background:linear-gradient(100deg,#2b3340,#5a6470 30%,#3a4350 55%,#6f7986 80%,#3e4652)}
.hero h1{position:absolute;left:0;right:0;top:82px;text-align:center;color:#fff;font-family:'Poppins',sans-serif;font-weight:700;font-size:29px}
.crumb{left:54px;top:339px;font-size:9px;display:flex;gap:7px}
.crumb .cur{color:var(--blue)}
.rule{left:54px;top:364px;width:700px;height:1px;background:var(--line)}
.box{border:1px solid var(--line);background:#fff}
.box h3{font-family:'Poppins',sans-serif;font-weight:400;font-size:15px;padding-bottom:9px;border-bottom:1px solid var(--line)}
.divs{left:54px;top:412px;width:221px;height:271px;padding:14px 18px}
.item{position:absolute;left:18px;width:184px;height:29px;background:var(--panel);font-size:8.7px;color:#444;display:flex;align-items:center;padding-left:17px;gap:6px}
.item.on{background:var(--blue);color:#fff}
.item svg{width:8px;height:9px}
.contact{left:54px;top:707px;width:221px;height:144px;padding:14px 18px}
.crow{display:flex;gap:10px;padding:12px 0 11px;border-bottom:1px solid var(--line);font-size:8.5px;color:var(--muted);line-height:1.4}
.crow:last-child{border-bottom:0}
.crow b{font-family:'Poppins',sans-serif;font-weight:500;color:var(--ink);font-size:9px}
.photo{left:292px;top:412px;width:461px;height:227px;background:linear-gradient(110deg,#a9cde0,#e4eff5 35%,#d2dde6 60%,#f3f4f6)}
.copy{left:292px;top:670px;width:462px;font-size:8.7px;font-weight:300;color:var(--muted);line-height:16.2px}
.quote{left:293px;top:785px;width:461px;height:60px;border:1px solid var(--line);box-shadow:0 0 4px rgba(0,0,0,.06)}
.quote p{position:absolute;left:52px;top:13px;right:18px;color:var(--blue);font-style:italic;font-size:10.3px;line-height:17px}
.quote .mark{position:absolute;left:15px;top:10px;color:#d8d8d8;font-family:'Poppins',sans-serif;font-weight:700;font-size:34px;line-height:1}
.footer{left:0;top:899px;width:805px;height:260px;background:var(--footer);color:var(--footer-text);font-size:8.7px}
.footer h4{font-family:'Poppins',sans-serif;font-weight:400;font-size:13px;color:#fff}
.fline{height:1px;background:#333}
.fbrand{left:54px;top:50px;display:flex;align-items:center;gap:5px;font-family:'Poppins',sans-serif;font-weight:600;font-size:9.5px;color:#fff}
.fbrand i{width:7px;height:7px;background:#fff;display:block}
.fcontact{left:54px;top:126px;line-height:17px}
.links{display:grid;grid-template-columns:120px 110px;row-gap:6px;line-height:12px}
.links span::before{content:"›";margin-right:5px}
.news{left:532px;top:113px;width:224px;line-height:16px}
.email{left:532px;top:155px;width:222px;height:31px;border:1px solid #444;display:flex;align-items:center;padding:0 10px;gap:8px;color:#bbb}
.circles{left:532px;top:205px;display:flex;gap:11px}
.circles i{width:27px;height:27px;border:1px solid #3d3d3d;border-radius:50%;display:block}
.bottom{left:0;top:1159px;width:805px;height:41px;background:var(--footer-bottom);color:var(--footer-text);font-size:8.7px}
</style>
</head>
<body>
<div class="abs topbar">
  <span class="abs dream">Looking for a dream job?</span>
  <span class="abs apply">APPLY NOW</span>
  <div class="abs toplinks"><span>Get Support</span><span>Job Career</span><span>Feedbacks</span><span>English ▾</span></div>
</div>

<div class="abs header"></div>
<div class="abs brand"><i></i>BRIGHT KELVO</div>
<svg class="abs" style="left:408px;top:58px" width="16" height="20" viewBox="0 0 16 20"><path d="M8 1a6.5 6.5 0 0 0-6.5 6.5C1.5 12 8 19 8 19s6.5-7 6.5-11.5A6.5 6.5 0 0 0 8 1z" fill="none" stroke="#1f3f9e" stroke-width="1.2"/><circle cx="8" cy="7.5" r="2.3" fill="none" stroke="#1f3f9e" stroke-width="1.2"/></svg>
<div class="abs info" style="left:434px;top:56px"><em>2450 Harbor Lane</em><br><b>Lakemont, VA, USA</b></div>
<svg class="abs" style="left:531px;top:58px" width="19" height="19" viewBox="0 0 20 20"><path d="M4 2l3 1 1 4-2 1.5a11 11 0 0 0 5.5 5.5L13 12l4 1 1 3-2 2C8 18 2 12 2 4z" fill="none" stroke="#1f3f9e" stroke-width="1.2"/><path d="M12 2a6 6 0 0 1 6 6M12 5a3 3 0 0 1 3 3" fill="none" stroke="#1f3f9e" stroke-width="1.2"/></svg>
<div class="abs info" style="left:559px;top:56px"><em>Quick Contact:</em><br><b>+1 555 010 2233</b></div>
<div class="abs join">JOIN NOW</div>

<div class="abs nav">
  <span>HOME</span><span>ABOUT US</span><span>SERVICES</span><span>CLIENTS</span><span>SOLUTIONS</span><span>JOIN US</span><span>CONTACT US</span>
  <div class="abs social">STAY CONNECTED: <i></i><i></i><i></i><i></i></div>
</div>

<div class="abs hero" role="img" aria-label="Collage of business people at work, shaking hands and using laptops, darkened"><h1>Healthcare Division</h1></div>

<div class="abs crumb"><span>Home</span><span>›</span><span>Our Divisions</span><span>›</span><span class="cur">Healthcare Division</span></div>
<div class="abs rule"></div>

<div class="abs box divs"><h3>Our Divisions</h3></div>
<div class="abs item" style="left:72px;top:472px"><svg viewBox="0 0 8 9"><path d="M.5.5h5l2 2v6h-7z" fill="none" stroke="currentColor" stroke-width=".8"/></svg>Finance</div>
<div class="abs item" style="left:72px;top:513px"><svg viewBox="0 0 8 9"><path d="M.5.5h5l2 2v6h-7z" fill="none" stroke="currentColor" stroke-width=".8"/></svg>Information Technology</div>
<div class="abs item on" style="left:72px;top:554px"><svg viewBox="0 0 8 9"><path d="M.5.5h5l2 2v6h-7z" fill="none" stroke="currentColor" stroke-width=".8"/></svg>Healthcare</div>
<div class="abs item" style="left:72px;top:595px"><svg viewBox="0 0 8 9"><path d="M.5.5h5l2 2v6h-7z" fill="none" stroke="currentColor" stroke-width=".8"/></svg>Government Projects</div>
<div class="abs item" style="left:72px;top:636px"><svg viewBox="0 0 8 9"><path d="M.5.5h5l2 2v6h-7z" fill="none" stroke="currentColor" stroke-width=".8"/></svg>Miscellaneous</div>

<div class="abs box contact">
  <h3>Contact Our Team</h3>
  <div class="crow"><svg width="12" height="14" viewBox="0 0 16 20"><path d="M8 1a6.5 6.5 0 0 0-6.5 6.5C1.5 12 8 19 8 19s6.5-7 6.5-11.5A6.5 6.5 0 0 0 8 1z" fill="none" stroke="#1f3f9e" stroke-width="1.3"/><circle cx="8" cy="7.5" r="2.3" fill="none" stroke="#1f3f9e" stroke-width="1.3"/></svg><div><b>Address:</b> 2450 Harbor Ln,<br>Lakemont, VA, USA</div></div>
  <div class="crow"><svg width="14" height="14" viewBox="0 0 20 20"><path d="M4 2l3 1 1 4-2 1.5a11 11 0 0 0 5.5 5.5L13 12l4 1 1 3-2 2C8 18 2 12 2 4z" fill="none" stroke="#1f3f9e" stroke-width="1.3"/></svg><div><b>Call Us:</b><br>+1 555 010 4471</div></div>
</div>

<div class="abs photo" role="img" aria-label="Doctor in white coat holding a tablet with floating healthcare icons around a central badge"></div>
<p class="abs copy">Not only do we provide services to the finance and technology world, we also service the healthcare industry with IT professionals as well. We understand the importance of having the right people behind the right projects you hire for, and that’s why our recruiting process is at a premium – it is our specialty to find you only the best candidates. Our Healthcare IT Division focuses specifically on partnering with Healthcare providers (hospitals, clinics, and physician practices) and healthcare payers (insurance companies) to provide IT professionals that meet the specific technology need or each individual client.</p>
<div class="abs quote"><span class="mark">“</span><p>Lorem Ipsum is simply dummy text of the printing and typesetting industry. Lorem Ipsum has been the industry's standard dummy text.</p></div>

<div class="abs footer">
  <div class="abs fbrand"><i></i>BRIGHT KELVO</div>
  <div class="abs fline" style="left:54px;top:86px;width:226px"></div>
  <div class="abs fcontact">⚲ Address: 2450 Harbor Ln, Lakemont, VA<br>☏ Phone: +1 555 010 8890<br>✉ Email: hello@brightkelvo.us<br>◷ Mon to Sat: 9.00 am to 5:00 pm</div>
  <h4 class="abs" style="left:292px;top:50px">Quick Links</h4>
  <div class="abs fline" style="left:292px;top:86px;width:230px"></div>
  <div class="abs links" style="left:292px;top:117px"><span>Home</span><span>Join Us</span><span>About Us</span><span>FAQs</span><span>Services</span><span>Testimonials</span><span>Clients</span><span>Job Career</span><span>Solutions</span><span>Meet Our Team</span><span>Contact Us</span><span>Privacy Policy</span></div>
  <h4 class="abs" style="left:532px;top:50px">Newsletter</h4>
  <div class="abs fline" style="left:532px;top:86px;width:230px"></div>
  <p class="abs news">Sign up today for get hints, tips, latest updates &amp; news of Bright Kelvo LLC.</p>
  <div class="abs email"><span>✉</span><span style="flex:1;border-left:1px solid #444;padding-left:8px">Email Address...</span><span>➤</span></div>
  <div class="abs circles"><i></i><i></i><i></i><i></i></div>
</div>
<div class="abs bottom"><span class="abs" style="left:54px;top:14px">Copyrights © 2022 Bright Kelvo LLC. All Rights Reserved.</span></div>
</body>
</html>
```